New B2C website design to help dads be better dads

KinQuest is a website to help dads be the “best dad you can be.”

We require our website to be designed into a PSD format, no coding necessary.

The general concept is a two-page design. The first page is the login page, the second page is the home page. Once at the home page, rather than navigating to and from different pages, the user will push and pull through different visual and functional layers of the hierarchy. In theory, this should add to the user experience by having a visual anchor of where they are (through layered pagination) as well as improving loading times since the new information should only be a delta in data load versus a brand new page load.

The general look-and-feel we are going for is clean, simple, minimal. This means that the winning design will show us a good eye for web-optimized typography, good use of white (negative) space, and good use of a visually pleasing grid.

We require a total of 6 page "views" plus the landing page. We note that many of the views are similar to one another.
Landing page
Milestone view
Task view
Content view, articles
Content view, products
Search view
What's new view

Please review all of the additional information provided as well as the attachments for examples.

We provide the following websites as good references for:

Typography:
http://dorvinlesk.com/journal/

Use of white space:
http://www.quartzheron.com/
http://glenmarrow.com/

Example for “scrolling” page concept as well as good balance of color, typography, and white space:
http://www.tovalumeet.eu/

Please contact us with questions so that we can guide your design effort.
Updates

Hello designers,

The following information is added to help guide the design process:

1.  For the text dialogue below the landing page, please assume the following word count:
"why are we making kin quest?": 250 words
"who are we?" 200 words
"what's the deal with the penguin logo?" 300 words

For the social media links, please see http://www.brimlecrates.com/
Notice the floating "social" bar that is always to the right.  This is the concept we are going for, please try to implement this as you see fit. 

Reason: Final design requests have been sent out to finalist designers, want to give everyone time to do a good job.

Target Market(s)

Fathers of young children ages 0-6 years old.

Industry/Entity Type

Product

Font styles to use
Sans Serif

Requirements
Must have
• Clean lines, minimal design concept

Incorporation of our logo (see attached document)

Header content is static for all views after landing page, see example

This page WILL be responsive, please keep that in mind when designing
The timeline bar should be to the left, with the timeline bar’s “milestones” also being responsive.

Designer is free to suggest font types, but any fonts used must be royalty-free and web-optimized. We request a minimum number of font types as well as fonts that load relatively fast. We reinforce that visually appealing typography is a significant factor in the winning design choice.

While we are not expecting the winning design to include code, please keep in mind that the final implementation needs to be optimized for desktop, tablet, and mobile platforms.

If you are using stock photography that is not generated by you, please provide where/how we can obtain imagery, as well as price.

All custom graphics must be available in original formats; Photoshop/GIMP layered files for layout design, and vector formats for logos, icons and other graphical elements.

Please incorporate “Blue” into design elements as you see fit, as the RGB 67 74 169 Blue is the primary color used in our brand. The complement to this blue is 255 202 0, a brownish orange. Feel free to use this color as well, although please keep it to a lesser amount.

Background color is your choice, do not feel the need to use the grey.
Should not have
• Excessive graphical content such that it affects loading times

Excessive use of too many font types such that it affects loading times

```html
<!DOCTYPE html>
<html lang="en">
<head>
<meta charset="utf-8">
<title>KinQuest – Home</title>
<link rel="stylesheet" href="https://fonts.googleapis.com/css2?family=Arvo&family=PT+Sans:wght@400;700&display=swap">
<style>
  :root {
    --brand-blue: #434aa9;
    --brand-gold: #ffca00;
    --welcome-orange: #e09a12;
    --page-bg: #f9f9f9;
    --header-bg: #ffffff;
    --rule: #d6d6d6;
    --line: #c9c9c9;
    --text-dark: #444444;
    --text-mid: #5c5c5c;
    --text-soft: #999999;
    --text-link: #888888;
    --icon-grey: #666666;
  }
  * { box-sizing: border-box; margin: 0; padding: 0; }
  html, body { width: 1200px; height: 994px; overflow: hidden; }
  body {
    position: relative;
    background: var(--page-bg);
    font-family: "PT Sans", sans-serif;
    color: var(--text-dark);
  }

  /* Header */
  .site-header {
    position: absolute; left: 0; top: 0; width: 1200px; height: 188px;
    background: var(--header-bg);
    border-bottom: 1px solid var(--rule);
  }
  .brand {
    position: absolute; left: 99px; top: 120px;
    display: flex; align-items: center; gap: 10px;
  }
  .brand-dot { width: 18px; height: 18px; border-radius: 50%; background: var(--brand-blue); }
  .brand-name {
    font-family: "PT Sans", sans-serif; font-weight: 700; font-size: 26px;
    color: var(--brand-blue); letter-spacing: 0.5px;
  }
  .welcome {
    position: absolute; right: 100px; top: 18px;
    font-family: "Arvo", serif; font-size: 26px; color: var(--welcome-orange);
  }
  .search {
    position: absolute; left: 703px; top: 77px; display: flex; gap: 8px;
  }
  .search-input {
    width: 305px; height: 34px; border: 1px solid #d8d8d8; border-radius: 2px;
    background: #fff; box-shadow: inset 0 2px 3px rgba(0,0,0,0.06);
    font-family: "PT Sans", sans-serif; font-size: 14px; color: var(--text-soft);
    padding: 0 14px; display: flex; align-items: center;
  }
  .search-button {
    width: 76px; height: 34px; border-radius: 2px;
    background: linear-gradient(#ffd43a, #f6b900);
    border: 1px solid #e8a900;
    font-family: "PT Sans", sans-serif; font-weight: 700; font-size: 14px;
    color: #a86a00; display: flex; align-items: center; justify-content: center;
  }
  .dad-score {
    position: absolute; left: 704px; top: 140px;
    display: flex; align-items: center; gap: 9px;
    font-size: 16px; color: var(--brand-blue);
  }
  .account-links {
    position: absolute; right: 109px; top: 140px;
    font-size: 15px; color: var(--text-link);
  }
  .account-links .sep { margin: 0 9px; }

  /* Timeline */
  .timeline-axis {
    position: absolute; left: 99px; top: 209px; width: 1px; height: 762px;
    background: var(--line);
  }
  .axis-cap { position: absolute; left: 94px; }
  .milestone {
    position: absolute; left: 0; display: flex; align-items: center;
  }
  .milestone-age {
    width: 93px; text-align: right; padding-right: 2px;
    font-size: 12px; color: var(--text-soft);
  }
  .milestone-icon { margin-left: 5px; }
  .milestone-title {
    margin-left: 15px; font-family: "Arvo", serif; font-size: 20px; color: var(--text-mid);
  }
  .milestone--open .milestone-title { font-size: 23px; }

  .sort {
    position: absolute; left: 907px; top: 220px; display: flex; align-items: center; gap: 8px;
    font-size: 13px; color: var(--text-link);
  }
  .sort-select {
    width: 138px; height: 29px; background: #fff; border: 1px solid #c8c8c8;
    display: flex; align-items: center; justify-content: space-between;
    padding: 0 10px; font-size: 13px; color: var(--text-dark);
  }
  .section-rule {
    position: absolute; left: 99px; top: 284px; width: 1002px; height: 1px; background: #cfcfcf;
  }

  /* Task list */
  .task-list {
    position: absolute; left: 131px; top: 284px; width: 285px; height: 428px;
    background: #fff; border: 1px solid #cfcfcf; border-top: none;
    list-style: none; padding-top: 2px;
  }
  .task {
    margin-left: 11px; width: 223px; height: 52px;
    border-bottom: 1px solid #e8e8e8;
    display: flex; align-items: center; gap: 11px; padding-left: 16px;
    font-size: 19px; color: var(--text-dark); white-space: nowrap;
  }
  .task:last-child { border-bottom: none; }
  .task-check {
    width: 12px; height: 12px; border: 1px solid #a9a9a9; background: #eee; flex: none;
    display: flex; align-items: center; justify-content: center;
  }

  /* Prompt */
  .milestone-prompt {
    position: absolute; left: 440px; top: 310px; width: 646px; text-align: center;
    font-family: "Arvo", serif;
  }
  .prompt-heading { font-size: 26px; line-height: 34px; color: var(--text-dark); font-weight: 400; }
  .prompt-body { margin-top: 10px; font-size: 16px; line-height: 27px; color: var(--text-soft); }

  /* Social rail */
  .social-rail {
    position: absolute; left: 1146px; top: 701px; width: 54px; height: 213px;
    background: var(--brand-blue); border-radius: 4px 0 0 4px;
    display: flex; flex-direction: column; align-items: center; justify-content: space-around;
    padding: 8px 0;
  }
  .social-link { width: 28px; height: 28px; border-radius: 50%; border: 2px solid #fff; }
  .social-link--solid { background: #fff; }
</style>
</head>
<body>

<header class="site-header">
  <div class="brand">
    <span class="brand-dot"></span>
    <span class="brand-name">KinQuest</span>
  </div>
  <h1 class="welcome">Welcome Greg, what would you like to do today?</h1>
  <form class="search">
    <div class="search-input">Keyword...</div>
    <div class="search-button">SEARCH</div>
  </form>
  <div class="dad-score">
    <svg width="12" height="11" viewBox="0 0 12 11"><path d="M6 11 1 6C-1 4 0 0 3 0c1.5 0 2.5 1 3 2C6.5 1 7.5 0 9 0c3 0 4 4 2 6z" fill="var(--brand-blue)"/></svg>
    <span>Super Dad Score: 10,500</span>
  </div>
  <nav class="account-links"><span>My Account</span><span class="sep">|</span><span>Log out</span></nav>
</header>

<div class="timeline-axis"></div>
<svg class="axis-cap" style="top:202px" width="11" height="7" viewBox="0 0 11 7"><path d="M1 6 5.5 1.5 10 6" fill="none" stroke="#b5b5b5" stroke-width="2"/></svg>
<svg class="axis-cap" style="top:967px" width="11" height="7" viewBox="0 0 11 7"><path d="M1 1 5.5 5.5 10 1" fill="none" stroke="#b5b5b5" stroke-width="2"/></svg>

<section class="milestone milestone--open" style="top:224px">
  <span class="milestone-age">-3 mo</span>
  <svg class="milestone-icon" width="18" height="18" viewBox="0 0 18 18"><circle cx="9" cy="9" r="9" fill="var(--icon-grey)"/><path d="M13 9H6M9 5.5 5.5 9 9 12.5" fill="none" stroke="#fff" stroke-width="2"/></svg>
  <h2 class="milestone-title">Prepare for the baby arrival</h2>
</section>

<div class="sort">
  <span>Sort by :</span>
  <div class="sort-select"><span>Most recent</span><svg width="9" height="5" viewBox="0 0 9 5"><path d="M0 0h9L4.5 5z" fill="#555"/></svg></div>
</div>
<div class="section-rule"></div>

<ul class="task-list">
  <li class="task"><span class="task-check"></span>Buy a crib</li>
  <li class="task"><span class="task-check"></span>Assemble the crib</li>
  <li class="task"><span class="task-check"></span>Buy a stroller</li>
  <li class="task"><span class="task-check"><svg width="9" height="8" viewBox="0 0 9 8"><path d="M1 4l2.5 2.5L8 1" fill="none" stroke="var(--brand-blue)" stroke-width="1.6"/></svg></span>Buy a carseat</li>
  <li class="task"><span class="task-check"></span>Install a carseat</li>
  <li class="task"><span class="task-check"></span>Learn to change a diaper</li>
  <li class="task"><span class="task-check"></span>Learn to hold a baby</li>
  <li class="task"><span class="task-check"></span>Set a fedding schedule</li>
</ul>

<article class="milestone-prompt">
  <h3 class="prompt-heading">Your big day is almost here! Do you have your go-back packed?</h3>
  <p class="prompt-body">Do you have your routes (plural!) to the hospital mapped out?<br>Lots to do, not much time!</p>
</article>

<section class="milestone" style="top:760px">
  <span class="milestone-age">0 mo</span>
  <svg class="milestone-icon" width="18" height="18" viewBox="0 0 18 18"><circle cx="9" cy="9" r="9" fill="var(--icon-grey)"/><path d="M5 9h7M9 5.5 12.5 9 9 12.5" fill="none" stroke="#fff" stroke-width="2"/></svg>
  <h2 class="milestone-title">What’s the Latest?</h2>
</section>

<section class="milestone" style="top:834px">
  <span class="milestone-age">0 mo</span>
  <svg class="milestone-icon" width="18" height="18" viewBox="0 0 18 18"><circle cx="9" cy="9" r="9" fill="var(--icon-grey)"/><path d="M5 9h7M9 5.5 12.5 9 9 12.5" fill="none" stroke="#fff" stroke-width="2"/></svg>
  <h2 class="milestone-title">What you searched for</h2>
</section>

<aside class="social-rail" aria-label="Share links">
  <span class="social-link social-link--solid"></span>
  <span class="social-link"></span>
  <span class="social-link"></span>
  <span class="social-link"></span>
</aside>

</body>
</html>
```